Home care agency

Current website QTRBLOOMS.com. Need to update and reformat to different pages. use my info from my current website

Target Market(s)

adult children

Industry/Entity Type

Home Health

Coding

Coded - Design and coding required

Number of Pages Required

4 page

Font styles to use
Sans Serif

Colors
3276b5
33a6d7
3277b5
85cae6
85acd3

```html
<!DOCTYPE html>
<html lang="en">
<head>
<meta charset="utf-8">
<title>QtrBlooms Home Health</title>
<link href="https://fonts.googleapis.com/css2?family=Open+Sans:wght@400;600;700&family=Raleway:wght@400;500;600&family=Montserrat:wght@800&display=swap" rel="stylesheet">
<style>
:root{
  --teal:#10b7b4;
  --teal-dark:#0e9e9b;
  --hero:#1f5c58;
  --orange:#f0a830;
  --ink:#2b2b2b;
  --muted:#9a9a9a;
  --soft:#f8f8f8;
  --grey:#eeeeee;
  --dark:#2b302e;
  --footer:#2f5f6d;
  --line:#e2e2e2;
}
*{margin:0;padding:0;box-sizing:border-box}
html,body{width:1200px;height:1200px;overflow:hidden;background:#fff}
body{font-family:"Open Sans",sans-serif;color:var(--ink)}
.stage{position:absolute;left:0;top:0;width:1932px;height:1932px;transform:scale(.62112);transform-origin:0 0}
.page{position:absolute;left:566px;top:0;width:800px;height:1932px;background:#fff}
.abs{position:absolute}
.h{font-family:"Raleway",sans-serif;font-weight:500;color:var(--ink)}
.p{font-size:6.6px;line-height:8.3px;color:var(--muted)}
.rule{position:absolute;width:24px;height:1.5px;background:var(--orange)}

/* hero */
.hero{position:absolute;left:0;top:0;width:800px;height:270px;background:radial-gradient(ellipse at 75% 45%,#3d7c6f 0%,#285f59 40%,#1d4f4d 100%)}
.hero::after{content:"";position:absolute;inset:0;background:rgba(16,90,90,.35)}
.nav{position:absolute;top:8px;left:450px;display:flex;gap:0;z-index:2}
.nav a{font-size:6px;color:#fff;text-decoration:none;padding:6px 6px;height:20px;display:block;font-weight:600}
.nav a.on{background:var(--teal-dark)}
.hero-brand{position:absolute;z-index:2;color:#fff;font-size:11px;font-weight:600;left:0;width:800px;text-align:center;top:104px}
.hero-brand i{display:inline-block;width:6px;height:6px;border:1px solid #fff;border-radius:50%;margin-right:4px;vertical-align:middle}
.hero-title{position:absolute;z-index:2;top:153px;left:0;width:800px;text-align:center;font-family:"Montserrat",sans-serif;font-weight:800;font-size:14.5px;color:#fff;letter-spacing:.3px}
.hero-text{position:absolute;z-index:2;top:180px;left:270px;width:260px;text-align:center;font-size:6.6px;line-height:8.3px;color:#fff}
.btn{position:absolute;z-index:2;background:var(--teal);color:#fff;font-size:5px;text-align:center;line-height:15px}

/* services */
.svc-title{font-size:6.6px;font-family:"Raleway",sans-serif;font-weight:500}
.list{font-size:6.6px;line-height:8.3px;color:var(--muted)}

/* band */
.band{position:absolute;left:156px;top:590px;width:488px;height:97px;background:var(--teal);color:#fff}
.band .col{position:absolute;top:0;height:97px}
.band .col+.col{border-left:1px solid rgba(255,255,255,.35)}
.band h4{font-family:"Raleway",sans-serif;font-weight:500;font-size:10px;position:absolute;top:16px}
.band p{position:absolute;top:38px;font-size:5.6px;line-height:8.3px;width:136px}
.band .more{position:absolute;top:74px;border:1px solid #fff;font-size:4.5px;padding:2px 3px}
.hours{position:absolute;top:39px;left:20px;width:98px;border:1px solid #fff;border-collapse:collapse;font-size:5.2px}
.hours td{border-bottom:1px solid rgba(255,255,255,.6);height:13.5px;padding-left:2px}

.round{position:absolute;width:16px;height:16px;border-radius:50%;background:var(--teal);color:#fff;font-size:7px;text-align:center;line-height:15px}

/* doctors */
.card{position:absolute;top:943px;width:110px;height:173px;border:1px solid var(--line);background:#fff}
.card .ph{position:absolute;left:3px;top:3px;width:104px;height:105px}
.card .nm{position:absolute;left:6px;top:119px;font-family:"Raleway",sans-serif;font-size:10px}
.card .rl{position:absolute;left:6px;top:137px;font-size:6.2px;color:#777}
.card .soc{position:absolute;left:6px;top:156px;display:flex;gap:5px}
.card .soc i{width:4px;height:4px;background:var(--teal-dark);display:block;border-radius:1px}

/* testimonials */
.quote{position:absolute;top:1201px;width:150px;height:49px;background:#fff;box-shadow:0 1px 3px rgba(0,0,0,.2);padding:6px 10px}
.quote::after{content:"";position:absolute;left:22px;bottom:-6px;border:6px solid transparent;border-top-color:#fff;border-bottom:0}
.av{position:absolute;top:1259px;width:20px;height:20px;border-radius:50%;background:linear-gradient(#8a9aa3,#c7a892)}
.who{position:absolute;top:1261px;font-family:"Raleway",sans-serif;font-size:9px;line-height:8px;color:#333}

/* form */
.field{position:absolute;left:325px;width:312px;height:15px;border:1px solid #ccc;font-size:5px;color:#999;padding:4px 5px}

/* footer */
.footer{position:absolute;left:0;top:1803px;width:800px;height:129px;background:var(--footer);color:#fff}
.footer h5{position:absolute;top:20px;font-size:7px;font-weight:600}
.footer p,.footer li{font-size:6.6px;line-height:8.3px}
.sq{position:absolute;top:46px;width:20px;height:20px}
</style>
</head>
<body>
<div class="stage">
<div class="page">

  <!-- hero -->
  <section class="hero" role="img" aria-label="Photo of a caregiver with a smiling elderly woman outdoors, tinted teal"></section>
  <div class="abs" style="left:186px;top:10px;width:14px;height:14px;border:1px solid #fff;border-radius:50%;z-index:2"></div>
  <nav class="nav">
    <a class="on">HOME</a><a>SERVICES</a><a>ABOUT</a><a>TESTIMONIAL</a><a>CONTACT</a>
  </nav>
  <div class="hero-brand"><i></i>QtrBlooms</div>
  <h1 class="hero-title">PROVIDING CARE THROUGHOUT THE SOUTH SHORE</h1>
  <p class="hero-text">Lorem ipsum dolor sit amet, consectetur adipisicing elit, sed do eiusmod tempor incididunt ut labore et dolore magna aliqua.</p>
  <div class="btn" style="left:365px;top:214px;width:70px;height:15px">Make an Appointment</div>
  <svg class="abs" style="left:400px;top:248px;z-index:2" width="10" height="7"><path d="M1 1l4 4 4-4" stroke="#fff" stroke-width="1.4" fill="none"/></svg>

  <!-- services -->
  <h2 class="h abs" style="left:162px;top:292px;font-size:12px">OUR SERVICE</h2>
  <div class="rule" style="left:162px;top:312px"></div>
  <h3 class="h abs" style="left:162px;top:321px;font-size:10px">Why Choose Home Care?</h3>
  <p class="p abs" style="left:162px;top:336px;width:150px">Home care is a cost-effective option that allows clients the ability to receive one-on-one care in the comfort of their own home. Home care also provides peace of mind to a client's family, near or far, without taking away a client's independence or privacy.</p>
  <h3 class="h abs" style="left:162px;top:394px;font-size:10px">Care Schedule/Frequency</h3>
  <p class="p abs" style="left:179px;top:409px;width:134px">QtrBlooms non-medical visits require a four hour minimum visit.</p>
  <p class="p abs" style="left:179px;top:434px;width:134px">There are no weekly minimum for medical or non-medical visits.</p>
  <p class="p abs" style="left:179px;top:459px;width:134px">Clients needing 24-hour care can save up 30% off of services by using a live-in caregiver. (Live-in caregiver requires personal bedroom and bathroom.)</p>

  <svg class="abs" style="left:325px;top:297px" width="16" height="16"><path d="M3 1v5a4 4 0 0 0 8 0V1M7 10v2a3 3 0 0 0 6 0V9" stroke="#10b7b4" stroke-width="1.5" fill="none"/><circle cx="13" cy="8" r="1.5" fill="#10b7b4"/></svg>
  <div class="svc-title abs" style="left:325px;top:328px">SKILLED CARE SERVICES</div>
  <div class="list abs" style="left:342px;top:347px">Free Initial Nursing Assessment<br>Medication Management<br>Wound Care<br>Injections<br>Medical Care Assistance<br>Transportation to Medical Appointments<br>Care Plan Management</div>
  <svg class="abs" style="left:325px;top:415px" width="20" height="16"><rect x="1" y="5" width="13" height="8" fill="#10b7b4"/><rect x="9" y="1" width="9" height="10" fill="#10b7b4"/><path d="M13.5 3v6M10.5 6h6" stroke="#fff" stroke-width="1.5"/><circle cx="4" cy="14" r="2" fill="#10b7b4"/><circle cx="12" cy="14" r="2" fill="#10b7b4"/></svg>
  <div class="svc-title abs" style="left:325px;top:447px">CLIENT BENEFITS</div>
  <div class="list abs" style="left:342px;top:465px;width:134px">Continuity of care with same caregiver for each client on a regular basis.<br>Open communication with owner by phone or email.<br>Ongoing communications to client's family by phone or email on a weekly basis (if desired.)<br>Streamlined payment process.</div>

  <svg class="abs" style="left:488px;top:297px" width="16" height="16"><circle cx="8" cy="4" r="3.5" fill="#10b7b4"/><path d="M1 16a7 7 0 0 1 14 0z" fill="#10b7b4"/><path d="M8 10v4M6 12h4" stroke="#fff" stroke-width="1.2"/></svg>
  <div class="svc-title abs" style="left:488px;top:328px">NON-MEDICAL SERVICES</div>
  <div class="list abs" style="left:504px;top:347px">Live-In Care<br>Respite Care<br>Assisting with Daily Living Activities<br>Meal Preparations</div>

  <!-- info band -->
  <section class="band">
    <div class="col" style="left:0;width:156px">
      <h4 style="left:15px">Emergency Case</h4>
      <p style="left:15px">I am text block. Edit this text from Appearance / Customize / Homepage header columns. Lorem ipsum dolor sit amet, consectetur adipiscing elit.</p>
      <span class="more" style="left:15px">READ MORE</span>
    </div>
    <div class="col" style="left:156px;width:163px">
      <h4 style="left:21px">Emergency Case</h4>
      <p style="left:21px">I am text block. Edit this text from Appearance / Customize / Homepage header columns. Lorem ipsum dolor sit amet, consectetur adipiscing elit.</p>
      <span class="more" style="left:21px">READ MORE</span>
    </div>
    <div class="col" style="left:319px;width:169px">
      <h4 style="left:20px">Opening Hours</h4>
      <table class="hours">
        <tr><td>Monday - Friday</td><td>9.00am - 5.00pm</td></tr>
        <tr><td>Saturday</td><td>9.30 - 17.30</td></tr>
        <tr><td>Sunday</td><td>9.30 - 15.00</td></tr>
      </table>
    </div>
  </section>

  <!-- dream -->
  <section class="abs" style="left:0;top:712px;width:800px;height:180px;background:var(--soft)"></section>
  <h2 class="h abs" style="left:162px;top:738px;font-size:12px;line-height:16px">THE BLOOMCARE<br>ULTIMATE DREAM</h2>
  <div class="rule" style="left:162px;top:777px"></div>
  <p class="p abs" style="left:162px;top:787px;width:110px">Lorem ipsum dolor sit amet, consectetur adipiscing elit, sed do eiusmod tempor incididunt ut labore et dolore magna aliqua..</p>
  <div class="abs" style="left:162px;top:829px;font-size:6.6px;color:var(--teal)">Know more..</div>
  <div class="round" style="left:291px;top:746px">›</div>
  <div class="round" style="left:291px;top:806px">›</div>
  <h3 class="h abs" style="left:324px;top:745px;font-size:10px">It's something important you want to know.</h3>
  <p class="p abs" style="left:324px;top:766px;width:200px">Lorem ipsum dolor sit amet, consectetur adipiscing elit, sed do eiusmod tempor incididunt ut labore et. Ut wisi enim ad minim veniam, quis nostrud.</p>
  <h3 class="h abs" style="left:324px;top:806px;font-size:10px">It's something important you want to know.</h3>
  <p class="p abs" style="left:324px;top:827px;width:200px">Lorem ipsum dolor sit amet, consectetur adipiscing elit, sed do eiusmod tempor incididunt ut labore et. Ut wisi enim ad minim veniam, quis nostrud.</p>

  <!-- doctors -->
  <h2 class="h abs" style="left:162px;top:914px;font-size:12px">MEET OUR DOCTORS!</h2>
  <div class="rule" style="left:162px;top:934px"></div>
  <div class="card" style="left:162px"><div class="ph" role="img" aria-label="Portrait of a female doctor in a white coat seated in an armchair" style="background:linear-gradient(#b08a6a,#8a5a40)"></div><div class="nm">Unknown</div><div class="rl">Doctor</div><div class="soc"><i></i><i></i><i></i></div></div>
  <div class="card" style="left:284px"><div class="ph" role="img" aria-label="Portrait of a male surgeon in blue scrubs, arms crossed" style="background:linear-gradient(#dfe7ee,#6f95c4)"></div><div class="nm">Unknown</div><div class="rl">Doctor</div><div class="soc"><i></i><i></i><i></i></div></div>
  <div class="card" style="left:406px"><div class="ph" role="img" aria-label="Portrait of a female nurse in a white uniform, arms crossed" style="background:linear-gradient(#ffffff,#eedfd6)"></div><div class="nm">Unknown</div><div class="rl">Doctor</div><div class="soc"><i></i><i></i><i></i></div></div>
  <div class="card" style="left:528px"><div class="ph" role="img" aria-label="Portrait of a male doctor with a stethoscope" style="background:linear-gradient(#f2f2f2,#d4d6d8)"></div><div class="nm">Unknown</div><div class="rl">Doctor</div><div class="soc"><i></i><i></i><i></i></div></div>

  <!-- testimonials -->
  <section class="abs" style="left:0;top:1150px;width:800px;height:157px;background:var(--grey)"></section>
  <h2 class="h abs" style="left:162px;top:1172px;font-size:12px">SEE WHAT PATIENTS ARE SAYING?</h2>
  <div class="rule" style="left:162px;top:1192px"></div>
  <div class="quote" style="left:162px"><p class="p">Lorem ipsum dolor sit amet, consectetur adipiscing elit, sed do eiusmod tempor incididunt ut labore et dolore magna aliqua.</p></div>
  <div class="quote" style="left:325px"><p class="p">Lorem ipsum dolor sit amet, consectetur adipiscing elit, sed do eiusmod tempor incididunt ut labore et dolore magna aliqua.</p></div>
  <div class="quote" style="left:488px"><p class="p">Lorem ipsum dolor sit amet, consectetur adipiscing elit, sed do eiusmod tempor incididunt ut labore et dolore magna aliqua.</p></div>
  <div class="av" style="left:162px" role="img" aria-label="Patient avatar"></div><div class="who" style="left:187px">Alex<br>&nbsp;Texas</div>
  <div class="av" style="left:325px" role="img" aria-label="Patient avatar"></div><div class="who" style="left:350px">Alex<br>&nbsp;Texas</div>
  <div class="av" style="left:488px" role="img" aria-label="Patient avatar"></div><div class="who" style="left:513px">Alex<br>&nbsp;Texas</div>

  <!-- about -->
  <section class="abs" style="left:0;top:1307px;width:800px;height:159px;background:var(--dark)"></section>
  <h2 class="h abs" style="left:162px;top:1334px;font-size:12px;line-height:16px;color:#fff;font-weight:600">« A FEW WORDS<br>ABOUT US »</h2>
  <p class="p abs" style="left:162px;top:1374px;width:476px;color:#8e8e8e">QtrBlooms Home Health Services is owned and operated by Marian Lowell. Marian is a registered nurse and has been in the health care system since 2001. She has specialized in home care, cardiology, trauma and critical care. She invests in future caregivers and has taught for the nursing programs at Eastbrook University, Harbor Health Institute, and Saint Clare College.</p>
  <p class="p abs" style="left:162px;top:1403px;width:476px;color:#8e8e8e">All QtrBlooms caregivers have extensive background checks and training regarding HIPAA compliance. We individualize the care of our clients in order to provide the best care possible in their home. QtrBlooms also ensures full access and understanding of client care at all times with a caregiver binder in the client's home at all times. This binder includes information on the client's care plan along and the notes from their caregivers. This will allow all caregivers and the client's family to have an understanding of the care being provided.</p>

  <!-- contact -->
  <h2 class="h abs" style="left:162px;top:1488px;font-size:12px">CONTACT US</h2>
  <div class="rule" style="left:162px;top:1516px"></div>
  <p class="p abs" style="left:162px;top:1526px;width:470px">Thank you for considering QtrBlooms for your care needs. Information about your medical conditions, care, and financial situation that you provide to us in writing, via email, on the phone (including information left on voice mails) is held in strictest confidence.</p>
  <h2 class="h abs" style="left:162px;top:1551px;font-size:12px">CONTACT ONLINE</h2>
  <div class="rule" style="left:162px;top:1580px"></div>
  <p class="p abs" style="left:162px;top:1589px">To contact us online, please fill out the care inquiry form below and you will be contacted within 24-48 hours.</p>
  <h3 class="h abs" style="left:162px;top:1609px;font-size:10px">Contact Info</h3>
  <h3 class="h abs" style="left:325px;top:1609px;font-size:10px">Having Any Query! Or Book an appointment</h3>
  <svg class="abs" style="left:166px;top:1638px" width="9" height="12"><path d="M4.5 11.5S1 7 1 4.5a3.5 3.5 0 0 1 7 0C8 7 4.5 11.5 4.5 11.5z" stroke="#888" fill="none"/><circle cx="4.5" cy="4.5" r="1.2" fill="#888"/></svg>
  <p class="p abs" style="left:184px;top:1638px">QtrBlooms Home Health Services<br>PO Box 48 Bayview, MA 02011</p>
  <svg class="abs" style="left:164px;top:1672px" width="14" height="11"><rect x=".5" y=".5" width="13" height="10" stroke="#888" fill="none"/><path d="M.5.5l6.5 5 6.5-5" stroke="#888" fill="none"/></svg>
  <p class="p abs" style="left:184px;top:1671px">info@qtrblooms.com</p>
  <svg class="abs" style="left:165px;top:1696px" width="11" height="11"><path d="M2 1l2.5 0 1 3-1.5 1a6 6 0 0 0 3 3l1-1.5 3 1V10A1 1 0 0 1 10 11 9 9 0 0 1 1 2a1 1 0 0 1 1-1z" fill="#888"/></svg>
  <p class="p abs" style="left:184px;top:1696px">+781-555-0142.</p>

  <div class="field" style="top:1638px">Your Name</div>
  <div class="field" style="top:1661px">Your Email</div>
  <div class="field" style="top:1684px">Subject</div>
  <div class="field" style="top:1706px;height:47px">Message</div>
  <div class="btn" style="left:325px;top:1761px;width:56px;height:16px;line-height:16px;font-size:5.5px">Send Message</div>

  <!-- footer -->
  <footer class="footer">
    <h5 style="left:162px">About Us</h5>
    <p class="abs" style="left:162px;top:41px;width:145px">Praesent convallis tortor et enim laoreet, vel consectetur purus latoque penatibus et dis parturient.</p>
    <h5 style="left:325px">Quick Links</h5>
    <ul class="abs" style="left:348px;top:41px">
      <li>Home</li><li>Service</li><li>Appointment</li>
    </ul>
    <h5 style="left:488px">Follow us</h5>
    <div class="sq" style="left:504px;background:#3a7fc1"></div>
    <div class="sq" style="left:527px;background:#d6483a"></div>
    <div class="sq" style="left:550px;background:#2c3f55"></div>
    <div class="sq" style="left:573px;background:#3ea3d8"></div>
    <p class="abs" style="left:0;top:101px;width:800px;text-align:center">© Copyright qtrblooms. All Rights Reserved</p>
  </footer>

</div>
</div>
</body>
</html>
```